Harbourline Sonography Academy (Kestrel Institute of Clinical Scanning) needs an additional web design f

Don't require a redesign of our existing website, I need an additional web design to compliment and feed into our existing web page (kics.edu.au) but establish excellent zintro rankings in it's own right. Web page is to appeal to a specific target market in the allied health industry who wish to learn how to do ultrasound on patients. New website is www. frontlinescanskills.com.au. Our educational institution delivers hands on workshops and seminars on ANYTHING involved with EMERGENCY Ultrasound - intro, advanced, doctors, nurses, etc. Our competitors in this field www.bedsidewavelabs.com.au and www.qpo.edu.au. Looking for a design that will capture the target audience and deliver the message that the courses are delivered by one of the best faculties in Australia. SEO strategies are paramount in that we don't wish to be penalised by Zintro by running a feeder site. Courses are delivered in Sydney and are accredited by an organisation called BRAV.com.au. The courses are listed under 2 qualifications on BRAV website - DLTX and KMRTE. Registrants of our courses are striving to achieve either DLTX - Certificate in Bedside Operator Sonography http://www.brav.com.au/newsite/Files/Documents/Education/DLTX/DLTX_Course_Brochure.pdf OR KMRTE - Certificate in Support Staff Operated Echography http://www.brav.com.au/newsite/Files/Documents/Education/KMRTE/KMRTE_Course_Brochure.pdf.
Website to be lumofon, smartphone and tablet compatible.

Target Market(s)

Emergency Physicians and Emergency nurses/doctors.

Industry/Entity Type

School

Coding

Coded - Design and coding required

Number of Pages Required

2 page

Other font styles liked:
• See website http://www.oakpointdental.com.au/

Colors
86cae6
ec1f27

Requirements
Must have
• Overall professional feel but easy to read and informative.
• Links to our normal website pages www.kics.edu.au
• Ability to rank high.
• Copy of material we deliver here http://www.kics.edu.au/emergency-ultrasound-course-1-3-days/ Click through on relevant dates for more information.
Nice to have
• I like this website - font, feel, layout etc.
• http://www.oakpointdental.com.au/
Should not have
• Information that will lower our zintro rankings knowing it is linked to www.kics.edu.au

```html
<!DOCTYPE html>
<html lang="en">
<head>
<meta charset="utf-8">
<title>Frontline Scan Skills</title>
<link href="https://fonts.googleapis.com/css2?family=Oswald:wght@400&family=Open+Sans:wght@400;600;700&display=swap" rel="stylesheet">
<style>
:root{
  --red:#ec1f27;
  --blue:#86cae6;
  --ink:#333333;
  --muted:#6b6b6b;
  --light:#f3f3f3;
  --line:#dcdcdc;
  --footer:#222222;
  --footer-text:#d8d8d8;
}
*{margin:0;padding:0;box-sizing:border-box}
html,body{width:1200px;height:2345px;overflow:hidden;background:#fff}
body{font-family:"Open Sans",Arial,sans-serif;color:var(--ink);position:relative}
.abs{position:absolute}
.heading{font-family:"Oswald","Arial Narrow",sans-serif;font-weight:400;font-size:31px;color:var(--red);line-height:1;white-space:nowrap}
.heading span{color:var(--blue)}
.rule{height:3px;background:#e6e6e6}
p.copy{font-size:13px;line-height:24px;color:var(--muted)}
.btn{background:var(--red);color:#fff;font-size:14px;font-weight:600;display:flex;align-items:center;justify-content:center}

/* header */
.topline{left:0;top:0;width:1200px;height:5px;background:var(--blue)}
.header{left:0;top:5px;width:1200px;height:102px;background:#f6f6f6}
.brand{left:133px;top:28px;font-family:"Oswald",sans-serif;font-size:34px;color:var(--red);letter-spacing:1px;line-height:1}
.brand-sub{left:133px;top:66px;font-size:20px;color:var(--blue);line-height:1}
.social-box{width:36px;height:36px;border:1px solid var(--line);background:#fff}
.search{left:844px;top:39px;width:225px;height:36px;background:#e9e9e9;display:flex;align-items:center}
.search span{font-size:13px;color:#999;font-style:italic;padding-left:12px;flex:1}
.search i{width:36px;height:36px;background:var(--blue);display:flex;align-items:center;justify-content:center}

.nav{left:0;top:107px;width:1200px;height:45px;background:var(--red);display:flex}
.nav ul{list-style:none;display:flex;margin-left:133px;height:45px}
.nav li{color:#fff;font-size:15px;padding:0 20px;display:flex;align-items:center}
.nav li.active{background:var(--blue)}

/* hero */
.hero{left:0;top:152px;width:1200px;height:469px;background:linear-gradient(100deg,#9aa3a8 0%,#c9d0d3 35%,#dfe3e6 60%,#c8b49a 100%)}
.hero-title{left:133px;top:299px;width:459px;height:68px;background:var(--blue);color:#fff;font-size:25px;display:flex;align-items:center;padding-left:14px}
.hero-text{left:133px;top:379px;width:459px;height:70px;background:#fff;border-left:4px solid var(--red);padding:13px 12px;font-size:12px;line-height:21px;color:#444}
.hero-btn{left:133px;top:461px;width:103px;height:33px}
.dots{left:133px;top:544px;display:flex;gap:8px}
.dots b{width:18px;height:18px;font-size:12px;font-weight:400;display:flex;align-items:center;justify-content:center;color:#fff}
.dots b.on{background:var(--blue)}

/* about */
.about-title{left:133px;top:665px}
.video-title{left:778px;top:665px}
.about-col{left:133px;top:717px;width:590px}
.divider-v{left:748px;top:730px;width:1px;height:170px;background:var(--line)}
.video{left:778px;top:725px;width:291px;height:195px;background:linear-gradient(135deg,#4a4f57,#8d7f86 55%,#3a3e45)}
.play{left:903px;top:790px;width:36px;height:36px;border-radius:50%;background:#fff}
.vbar{left:778px;top:893px;width:291px;height:27px;background:#111;display:flex;align-items:center;gap:10px;padding:0 8px;color:#ddd;font-size:11px}

/* features */
.features{left:0;top:957px;width:1200px;height:378px;background:var(--light)}
.feat-title{top:1010px;left:0;width:1200px;text-align:center}
.feature{width:230px;text-align:center}
.feature .ring{width:116px;height:116px;border-radius:50%;background:#fff;border:7px solid #e1e1e1;margin:0 auto;display:flex;align-items:center;justify-content:center}
.feature p{margin-top:28px;font-size:16px;line-height:23px;color:#444}
.fsep{width:1px;height:150px;background:#e2e2e2;top:1110px}

/* news & courses */
.date{width:55px;height:55px;background:var(--blue);color:#fff;text-align:center;line-height:1}
.date b{display:block;font-size:25px;font-weight:400;padding-top:6px}
.date small{font-size:10px}
.news{left:203px;width:400px;font-size:13px;line-height:26px;color:var(--muted)}
.news strong{color:#222;font-size:12.5px;white-space:nowrap}
.tabs{left:635px;top:1442px;display:flex;gap:4px}
.tab{height:43px;padding:0 8px;font-size:13px;display:flex;align-items:center;background:#ededed;border:1px solid var(--line);color:#444}
.tab.on{background:var(--blue);color:#fff;font-weight:600}
.panel{left:635px;top:1485px;width:434px;height:141px;background:#f1f1f1;border:1px solid var(--line)}
.doc-ph{left:645px;top:1492px;width:80px;height:130px;background:linear-gradient(180deg,#d9c1a8,#e7eef2 40%,#b9c7d1)}
.panel-text{left:765px;top:1498px;width:296px;font-size:13px;line-height:23px;color:var(--muted)}
.more{left:976px;top:1597px;font-size:13px;color:var(--red)}

/* seminars */
.seminars{left:0;top:1665px;width:1200px;height:225px;background:var(--light)}
.sem-title{top:1698px;left:0;width:1200px;text-align:center}
.thumb{width:55px;height:55px;background:linear-gradient(135deg,#e7d6c6,#b9b2ae)}
.sem{width:400px;font-size:13px;line-height:25px;color:var(--muted)}
.sem em{color:var(--red);font-size:12.5px}
.sem strong{color:#222;font-size:12.5px;white-space:nowrap}

/* partners */
.partner-title{left:133px;top:1948px}
.pbox{width:127px;height:65px;top:1934px;border:1px solid var(--line);background:#fff;display:flex;align-items:center;justify-content:center}
.pbox i{width:34px;height:34px;background:#d4d8de;border-radius:4px}

/* footer */
.footer{left:0;top:2038px;width:1200px;height:307px;background:var(--footer)}
.fhead{font-size:18px;font-weight:600;color:#fff}
.flinks{list-style:none;font-size:13px;line-height:25px;color:var(--footer-text)}
.flinks li::before{content:"›";color:#888;margin-right:8px}
.contact{left:453px;font-size:13px;line-height:19px;color:var(--footer-text);white-space:nowrap}
.map{left:742px;top:2093px;width:327px;height:168px;background:linear-gradient(135deg,#ece9e2,#e2ddd4)}
.fline{left:133px;top:2281px;width:936px;height:1px;background:#3a3a3a}
.copyright{left:133px;top:2302px;font-size:12px;color:var(--footer-text)}
.fsoc{width:36px;height:36px;border:1px solid #555;top:2293px}
</style>
</head>
<body>

<div class="abs topline"></div>
<header class="abs header"></header>
<div class="abs brand">FRONTLINE</div>
<div class="abs brand-sub">Frontline Scan Skills</div>
<div class="abs social-box" style="left:706px;top:39px" aria-label="social link"></div>
<div class="abs social-box" style="left:749px;top:39px" aria-label="social link"></div>
<div class="abs social-box" style="left:792px;top:39px" aria-label="social link"></div>
<div class="abs search"><span>Search</span><i><svg width="16" height="16" viewBox="0 0 16 16"><circle cx="6.5" cy="6.5" r="4.8" fill="none" stroke="#fff" stroke-width="2"/><line x1="10" y1="10" x2="14.5" y2="14.5" stroke="#fff" stroke-width="2.4"/></svg></i></div>

<nav class="abs nav"><ul>
<li class="active">Home</li><li>About Us</li><li>Seminars</li><li>Become a Sonographer</li><li>Consulting</li><li>Models</li><li>Information</li><li>Contact Us</li>
</ul></nav>

<div class="abs hero" role="img" aria-label="Photo of a sonographer seated at an ultrasound machine in a clinic"></div>
<div class="abs hero-title">Courses To Meet Your Traning Needs</div>
<div class="abs hero-text">Lorem ipsum dolor sit amet, consectetuer adipiscing elit, sed diam nonummy nibh euismod tincidunt ut laoreet dolore magna aliquam erat volutpat.</div>
<div class="abs btn hero-btn">Read More</div>
<div class="abs dots"><b class="on">1</b><b>2</b><b>3</b></div>

<h2 class="abs heading about-title">About Frontline <span>Scan Skills</span></h2>
<div class="abs rule" style="left:133px;top:707px;width:590px"></div>
<div class="abs about-col">
<p class="copy">Lorem ipsum dolor sit amet, consectetuer adipiscing elit, sed diam nonummy nibh euismod tincidunt ut laoreet dolore magna aliquam erat volutpat. Ut wisi enim ad minim veniam, quis nostrud exerci tation ullamcorper suscipit lobortis nisl ut aliquip ex ea commodo consequat.</p>
<p class="copy" style="margin-top:22px">Duis autem vel eum iriure dolor in hendrerit in vulputate velit esse molestie consequat, vel illum dolore eu feugiat nulla facilisis at vero eros et accumsan et iusto odio dignissim qui blandit praesent luptatum zzril delenit augue duis dolore te feugait nulla facilisi.</p>
<div class="btn" style="width:94px;height:33px;margin-top:12px">Read More</div>
</div>
<div class="abs divider-v"></div>
<h2 class="abs heading video-title">Watch <span>Our Video</span></h2>
<div class="abs rule" style="left:778px;top:707px;width:291px"></div>
<div class="abs video" role="img" aria-label="Video still of trainees at an ultrasound workstation"></div>
<div class="abs play"><svg width="36" height="36" viewBox="0 0 36 36"><path d="M14 11 L26 18 L14 25Z" fill="#222"/></svg></div>
<div class="abs vbar"><svg width="10" height="12" viewBox="0 0 10 12"><path d="M0 0L10 6L0 12Z" fill="#fff"/></svg><span>04:59</span><div style="flex:1;height:5px;background:#555;border-radius:3px"></div><span>10:35</span><svg width="12" height="12" viewBox="0 0 12 12"><path d="M0 4H3L7 1V11L3 8H0Z" fill="#fff"/></svg></div>

<section class="abs features"></section>
<h2 class="abs heading feat-title">Features of <span>Cources</span></h2>
<div class="abs rule" style="left:450px;top:1050px;width:300px"></div>
<div class="abs feature" style="left:133px;top:1102px"><div class="ring"><svg width="50" height="50" viewBox="0 0 50 50" fill="none" stroke="#ec1f27" stroke-width="2.5"><rect x="5" y="8" width="40" height="26" rx="2"/><line x1="25" y1="34" x2="25" y2="42"/><line x1="16" y1="42" x2="34" y2="42"/></svg></div><p>Online Lectures<br>Prerequisite physics</p></div>
<div class="abs feature" style="left:366px;top:1102px"><div class="ring"><svg width="50" height="50" viewBox="0 0 50 50" fill="none" stroke="#ec1f27" stroke-width="2.5"><circle cx="25" cy="18" r="11"/><line x1="20" y1="30" x2="20" y2="40"/><line x1="30" y1="30" x2="30" y2="40"/><line x1="20" y1="40" x2="30" y2="40"/></svg></div><p>Maximal hands<br>on scanning time</p></div>
<div class="abs feature" style="left:602px;top:1102px"><div class="ring"><svg width="50" height="50" viewBox="0 0 50 50" fill="none" stroke="#ec1f27" stroke-width="2.5"><rect x="10" y="6" width="28" height="38" rx="2"/><line x1="16" y1="16" x2="32" y2="16"/><line x1="16" y1="24" x2="32" y2="24"/><line x1="16" y1="32" x2="26" y2="32"/></svg></div><p>Structured<br>Reports</p></div>
<div class="abs feature" style="left:837px;top:1102px"><div class="ring"><svg width="50" height="50" viewBox="0 0 50 50" fill="none" stroke="#ec1f27" stroke-width="2.5"><path d="M25 12 C18 8 10 8 5 10 V40 C10 38 18 38 25 42 C32 38 40 38 45 40 V10 C40 8 32 8 25 12Z"/><line x1="25" y1="12" x2="25" y2="42"/></svg></div><p>Opportunity for<br>Logbook submission</p></div>
<div class="abs fsep" style="left:366px"></div>
<div class="abs fsep" style="left:600px"></div>
<div class="abs fsep" style="left:835px"></div>

<h2 class="abs heading" style="left:133px;top:1382px">Latest News <span>&amp; Events</span></h2>
<div class="abs rule" style="left:133px;top:1420px;width:300px"></div>
<div class="abs date" style="left:133px;top:1450px"><b>25</b><small>SEP</small></div>
<div class="abs news" style="top:1440px"><strong>Lorem ipsum dolor sit amet, consectetu Ut wisi enim ad</strong><br>minim ven nostrud exerci tation ullamcorper suscipit<br>lobortis nis ut aliquip commodokl consequat.</div>
<div class="abs date" style="left:133px;top:1555px"><b>25</b><small>SEP</small></div>
<div class="abs news" style="top:1545px"><strong>Lorem ipsum dolor sit amet, consectetu Ut wisi enim ad</strong><br>minim ven nostrud exerci tation ullamcorper suscipit<br>lobortis nis ut aliquip commodokl consequat.</div>

<h2 class="abs heading" style="left:628px;top:1382px">Our <span>Courses</span></h2>
<div class="abs rule" style="left:628px;top:1420px;width:300px"></div>
<div class="abs tabs"><div class="tab on">Emergency Physicians</div><div class="tab">Sonographers</div><div class="tab">Medical Educationalists</div></div>
<div class="abs panel"></div>
<div class="abs doc-ph" role="img" aria-label="Photo of a physician holding a clipboard"></div>
<div class="abs panel-text">(with post graduate Ultrasound qualifications) Lorem ipsum dolor sit amet, consectetuer adipiscing elit, sed diam nonummy nibh euismod tincidunt ut laoreet dolore magna</div>
<div class="abs more">Read More ››</div>

<section class="abs seminars"></section>
<h2 class="abs heading sem-title">Upcoming <span>Seminar</span></h2>
<div class="abs rule" style="left:450px;top:1737px;width:300px"></div>
<svg class="abs" style="left:92px;top:1795px" width="22" height="42" viewBox="0 0 22 42"><path d="M20 2 L3 21 L20 40" fill="none" stroke="#ec1f27" stroke-width="2"/></svg>
<svg class="abs" style="left:1086px;top:1795px" width="22" height="42" viewBox="0 0 22 42"><path d="M2 2 L19 21 L2 40" fill="none" stroke="#ec1f27" stroke-width="2"/></svg>
<div class="abs thumb" style="left:133px;top:1772px" role="img" aria-label="Seminar photo"></div>
<div class="abs sem" style="left:203px;top:1762px"><em>25/08/2014 | 4:30 pm</em><br><strong>Lorem ipsum dolor sit amet, consectetu Ut wisi enim ad</strong><br>minim ven nostrud exerci tation ullamcorper suscipit<br>lobortis nis ut aliquip commodokl consequat.</div>
<div class="abs thumb" style="left:600px;top:1772px" role="img" aria-label="Seminar photo"></div>
<div class="abs sem" style="left:670px;top:1762px"><em>25/08/2014 | 4:30 pm</em><br><strong>Lorem ipsum dolor sit amet, consectetu Ut wisi enim ad</strong><br>minim ven nostrud exerci tation ullamcorper suscipit lobortis<br>nis ut aliquip commodokl consequat.</div>

<h2 class="abs heading partner-title">Our <span>Partner</span></h2>
<svg class="abs" style="left:284px;top:1947px" width="22" height="40" viewBox="0 0 22 40"><path d="M20 2 L3 20 L20 38" fill="none" stroke="#ec1f27" stroke-width="2"/></svg>
<svg class="abs" style="left:1046px;top:1947px" width="22" height="40" viewBox="0 0 22 40"><path d="M2 2 L19 20 L2 38" fill="none" stroke="#ec1f27" stroke-width="2"/></svg>
<div class="abs pbox" style="left:322px" aria-label="Partner"><i></i></div>
<div class="abs pbox" style="left:469px" aria-label="Partner"><i></i></div>
<div class="abs pbox" style="left:615px" aria-label="Partner"><i style="border-radius:50%"></i></div>
<div class="abs pbox" style="left:760px" aria-label="Partner"><i></i></div>
<div class="abs pbox" style="left:907px" aria-label="Partner"><i></i></div>

<footer class="abs footer"></footer>
<div class="abs fhead" style="left:133px;top:2077px">Quick Links</div>
<div class="abs" style="left:133px;top:2105px;width:280px;height:1px;background:#3a3a3a"></div>
<ul class="abs flinks" style="left:133px;top:2128px"><li>Home</li><li>About Us</li><li>Seminars</li><li>Become a Sonographer</li><li>Consulting</li></ul>
<ul class="abs flinks" style="left:313px;top:2128px"><li>Models</li><li>Information</li><li>Contact Us</li></ul>
<div class="abs fhead" style="left:453px;top:2077px">Contact Us</div>
<div class="abs" style="left:453px;top:2105px;width:260px;height:1px;background:#3a3a3a"></div>
<svg class="abs" style="left:453px;top:2134px" width="14" height="18" viewBox="0 0 14 18"><path d="M7 0C3 0 0 3 0 7C0 12 7 18 7 18S14 12 14 7C14 3 11 0 7 0Z" fill="#86cae6"/><circle cx="7" cy="7" r="2.5" fill="#222"/></svg>
<div class="abs contact" style="top:2132px;left:480px"><b style="color:#fff">Frontline Scan Skills</b><br>Level 3, 48 Corrella Lane<br>Wattlebrook NSW, 2094</div>
<svg class="abs" style="left:453px;top:2210px" width="14" height="14" viewBox="0 0 14 14"><path d="M3 0L5 4L3.5 5.5C4.5 7.5 6.5 9.5 8.5 10.5L10 9L14 11L13 14C6 14 0 8 0 1Z" fill="#86cae6"/></svg>
<div class="abs contact" style="top:2207px;left:480px">+ 61 2 9000 4172</div>
<svg class="abs" style="left:453px;top:2242px" width="14" height="11" viewBox="0 0 14 11"><rect width="14" height="11" fill="#86cae6"/><path d="M0 0L7 6L14 0" fill="none" stroke="#222" stroke-width="1.4"/></svg>
<div class="abs contact" style="top:2238px;left:480px">admin@frontlinescanskills.com.au</div>
<div class="abs map" role="img" aria-label="Street map showing the academy location"></div>
<svg class="abs" style="left:893px;top:2140px" width="22" height="30" viewBox="0 0 22 30"><path d="M11 0C5 0 0 5 0 11C0 19 11 30 11 30S22 19 22 11C22 5 17 0 11 0Z" fill="#ec1f27"/><circle cx="11" cy="11" r="4" fill="#fff"/></svg>
<div class="abs fline"></div>
<div class="abs copyright">Copyright © 2014 Frontline Scan Skills. All Rights Reserved.</div>
<div class="abs fsoc" style="left:940px" aria-label="social link"></div>
<div class="abs fsoc" style="left:986px" aria-label="social link"></div>
<div class="abs fsoc" style="left:1032px" aria-label="social link"></div>

</body>
</html>
```